Croatia Luxury Cruise Brochure

1) Front page instead of By Orchard Path with Liesl please put by Pinecrest Harbor Guild – same on the last page where you have her contacts
2) Can you please add into the second page where you have ‘Welcome to your Croatia trip’ itinerary at glance. You can put it just below the text you have. Create a nice looking table .
D1 August 05, 2023 Arrival to Dubrovnik , Welcome cocktail party on Dubrovnik city walls
D2 August 06, 2023 Dubrovnik Highlights city tour – Embark sail to Elafiti
D3 August 07, 2023 Sail to Mljet island and day at leisure at sea
D4 August 08, 2023 Peljesac Wine Tasting with Live Music – Sail to Korcula
D5 August 09, 2023 Korcula Highlights Explorer Tour & Local Estate Dinner
D6 August 10, 2023 Korcula to Vis Island sail
D7 August 11, 2023 Vis Militarty Tour -sail to Pakleni Islands Bortelli sunset cocktails
D8 August 12, 2023 Hvar island – sail to Split
D9 August 13, 2023 Disembark – Split & Trogir ORVALD tours with 6-course wine dinner
D10 August 14, 2023 Fly out
Note: All tours & Experiences are optional add ons except the Cocktail reception on Dubrovnik city walls
3) Changes to the itinerary:
D1 is now arrival to Dubrovnik day earlier (AUGU5) and the rest is all moved accordingly. Please check the link
https://portal.kelvoro-desk. com/itinerary/custom-trip-prepared-for-liesl-group/
4) Inclusion/Exclusion page we need to update a little. Please make 3 different categories with a note for booking conditions.
Inclusions
• All transfers per itinerary including airport pick up and drop off
• 7 nights cruise on MS Dovetail on half board basis
• All meals stated per itinerary
• Captains dinner
• Unlimited water
• Masseuse on board
• Service of 11 crew members
• Cruise director
• Unlimited WiFi
• Daily cleaning
• Arrival refreshments
• Premium docking
• Usage of non motorized water toys
• Exclusive cocktail reception on Dubrovnik city walls with live music and snacks
Optional Tours
• Dubrovnik Highlights Explorer tour
• Peljesac Wine tour with live music
• Korcula explorer tour with local estate dinner
• Vis Military tour
• Bortelli Lounge bar reservation (min spend EUR100 per person)
• Split & Trogir ORVALD Explorer tour
• 6-course farewell dinner with local wine pairing
• 1 night post stay in Velmont 5* hotel in Split (This is added on optional)
Extras
• Tips for the crew
• Beverage consumption
• Usage of motorized water toys – EUR150 per hour
• International flights
• Any personal expenses
Booking conditions
30 % non-refundable deposit needed upon confirmation
Balance of the trip and any optional tours picked are due 06 May, 2023
Luxury travelers from USA and Canada
Tourism

```html
<!DOCTYPE html>
<html lang="en">
<head>
<meta charset="utf-8">
<title>Croatia Luxury Cruise Brochure</title>
<link href="https://fonts.googleapis.com/css2?family=Montserrat:wght@400;600;700;800;900&family=Open+Sans:wght@400;600;700&display=swap" rel="stylesheet">
<style>
:root{
  --navy:#1c2a3e;
  --navy-deep:#131e2d;
  --red:#b3141d;
  --grey:#5f6670;
  --rule:#d9dce0;
  --row:#f3f4f6;
  --paper:#ffffff;
  --canvas:#ffffff;
}
*{box-sizing:border-box;margin:0;padding:0}
html,body{width:1200px;height:2256px;overflow:hidden;background:var(--canvas)}
.canvas{position:relative;width:1200px;height:2256px;overflow:hidden;font-family:"Open Sans",Arial,sans-serif;color:var(--grey)}
.page{position:absolute;width:290px;height:400px;background:var(--paper);box-shadow:0 1px 5px rgba(0,0,0,.28);overflow:hidden}
.page::after{content:"";position:absolute;right:0;bottom:0;width:34px;height:14px;background:var(--red);clip-path:polygon(40% 0,100% 0,100% 100%,0 100%)}
.brand{position:absolute;top:14px;right:14px;font-family:"Montserrat",sans-serif;font-weight:900;font-size:12px;letter-spacing:1px;color:var(--red)}
.head{padding:14px 90px 6px 14px}
.kicker{font-family:"Montserrat",sans-serif;font-weight:700;font-size:5.5px;letter-spacing:.6px;color:var(--red);text-transform:uppercase}
.title{font-family:"Montserrat",sans-serif;font-weight:900;font-size:21px;color:var(--navy);line-height:1;text-transform:uppercase;white-space:nowrap}
.title-sm{font-size:15px}
.title-xs{font-size:13px}
.title-rule{height:2px;width:60px;background:var(--red);margin-top:4px}
.body{font-size:5px;line-height:1.5;color:var(--grey)}
.body p+p{margin-top:3px}
.lead{font-size:5.6px;line-height:1.45;color:var(--red);font-weight:600;margin-bottom:4px}
.photo{border-radius:1px}
.ph-city{background:linear-gradient(160deg,#c99b6a,#b86d44 45%,#5e8fae)}
.ph-sea{background:linear-gradient(170deg,#8fc3dc,#3f7fa6 55%,#2a5876)}
.ph-island{background:linear-gradient(170deg,#a8cde0,#5a9b8a 50%,#3d6a4b)}
.ph-ship{background:linear-gradient(175deg,#b5d4e6,#e9eef2 45%,#2f6d93 70%,#1f4e6d)}
.ph-stone{background:linear-gradient(160deg,#e1cfae,#b99669 55%,#7b8f9e)}
.ph-dine{background:linear-gradient(150deg,#5a3c2c,#a7744b 50%,#e4c79e)}
.ph-green{background:linear-gradient(165deg,#9fc78c,#4f8a4a 50%,#2d5a3a)}
.day{display:grid;grid-template-columns:1fr 96px;gap:8px;padding:6px 14px}
.day-top{display:flex;align-items:flex-start;gap:5px;margin-bottom:4px}
.num{flex:none;width:13px;height:13px;background:var(--red);color:#fff;font-family:"Montserrat",sans-serif;font-weight:800;font-size:7px;display:flex;align-items:center;justify-content:center}
.day-title{font-family:"Montserrat",sans-serif;font-weight:800;font-size:6px;line-height:1.25;color:var(--navy);text-transform:uppercase}
.day .photo{height:82px}
.divider{height:1px;background:var(--rule);margin:2px 14px}

/* glance table */
.glance{margin:6px 14px 0}
.glance-h{font-family:"Montserrat",sans-serif;font-weight:800;font-size:6.5px;color:var(--navy);text-transform:uppercase;margin-bottom:3px}
.glance table{width:100%;border-collapse:collapse;font-size:4.6px;line-height:1.3}
.glance th{background:var(--navy);color:#fff;font-family:"Montserrat",sans-serif;font-weight:700;font-size:4.6px;text-transform:uppercase;text-align:left;padding:2px 3px}
.glance td{padding:1.8px 3px;border-bottom:1px solid var(--rule);vertical-align:top}
.glance tr:nth-child(even) td{background:var(--row)}
.glance td.d{width:14px;color:#fff;background:var(--red)!important;font-family:"Montserrat",sans-serif;font-weight:800;text-align:center}
.glance td.date{width:52px;font-weight:700;color:var(--navy);white-space:nowrap}
.glance-note{font-size:4.4px;font-style:italic;margin-top:3px;color:var(--grey)}

/* cover */
.cover{background:var(--navy-deep)}
.cover .photo{position:absolute;left:0;top:0;width:290px;height:250px;background:linear-gradient(180deg,#20344e 0%,#3f6f8f 40%,#b58a5b 75%,var(--navy-deep) 100%)}
.cover-title{position:absolute;top:20px;left:0;width:100%;text-align:center;font-family:"Montserrat",sans-serif;font-weight:900;font-size:44px;letter-spacing:2px;color:#fff}
.cover-box{position:absolute;left:120px;top:170px;width:150px;padding:8px;background:var(--red);color:#fff;font-family:"Montserrat",sans-serif;text-align:center}
.cover-box .big{font-weight:800;font-size:10px;line-height:1.15;text-transform:uppercase}
.cover-box .yr{font-weight:900;font-size:22px;margin-top:3px}
.cover-dates{position:absolute;left:120px;top:258px;width:150px;text-align:center;font-family:"Montserrat",sans-serif;font-weight:600;font-size:6.5px;color:#fff;line-height:1.6}
.cover-logo{position:absolute;left:0;width:100%;text-align:center;bottom:44px;font-family:"Montserrat",sans-serif;font-weight:900;font-size:22px;letter-spacing:2px;color:#fff}
.cover-url{position:absolute;left:0;width:100%;text-align:center;bottom:26px;font-size:5.5px;color:#c9d0d8}

/* contact page */
.contact-block{position:absolute;top:44px;left:0;width:100%;text-align:center}
.phone{font-family:"Montserrat",sans-serif;font-weight:800;font-size:12px;color:var(--navy)}
.contact-block .body{width:200px;margin:6px auto 0}

/* price */
.price-box{margin:6px 14px;background:var(--red);color:#fff;display:flex;align-items:center;gap:8px;padding:6px 8px;font-family:"Montserrat",sans-serif}
.price-box .yr{font-weight:900;font-size:20px}
.price-box .txt{font-weight:700;font-size:6.5px;line-height:1.3;text-transform:uppercase}
.grid2{display:grid;grid-template-columns:1fr 1fr;gap:4px;padding:4px 14px}
.grid2 .photo{height:58px}

/* inclusions */
.list-h{font-family:"Montserrat",sans-serif;font-weight:800;font-size:6px;color:var(--navy);text-transform:uppercase;margin:4px 0 2px}
.list{list-style:none;font-size:4.6px;line-height:1.45}
.list li{padding-left:6px;position:relative}
.list li::before{content:"";position:absolute;left:0;top:2px;width:2.5px;height:2.5px;background:var(--red)}
.cols{display:grid;grid-template-columns:1fr 1fr;gap:8px;padding:0 14px}
</style>
</head>
<body>
<div class="canvas">

  <!-- Cover -->
  <section class="page cover" style="left:308px;top:20px">
    <div class="photo" role="img" aria-label="Photo of Dubrovnik fortress walls above the Adriatic"></div>
    <div class="cover-title">CROATIA</div>
    <div class="cover-box">
      <div class="big">Luxury yacht cruise<br>on MS Dovetail</div>
      <div class="yr">2023</div>
    </div>
    <div class="cover-dates">AUG 05 – AUG 14<br>by Pinecrest Harbor Guild</div>
    <div class="cover-logo">KELVORO</div>
    <div class="cover-url">www.kelvoro-desk.com</div>
  </section>

  <!-- Contact page -->
  <section class="page" style="left:640px;top:20px">
    <div class="brand">KELVORO</div>
    <div class="contact-block">
      <div class="phone">+1 800 555 0142</div>
      <div class="body"><p>Pinecrest Harbor Guild · www.kelvoro-desk.com<br>Your private yacht journey along the Dalmatian coast, planned for Liesl and group.</p></div>
    </div>
    <div class="photo ph-ship" style="position:absolute;left:0;top:130px;width:290px;height:230px" role="img" aria-label="Photo of the yacht MS Dovetail at anchor near an island"></div>
  </section>

  <!-- About Croatia -->
  <section class="page" style="left:92px;top:450px">
    <div class="brand">KELVORO</div>
    <div class="head"><div class="title title-sm">About Croatia</div><div class="title-rule"></div></div>
    <div style="padding:2px 14px" class="body">
      <div class="lead">Welcome to your Croatia trip – the perfect setting for the ultimate island hopping experience.</div>
      <p>Croatia stretches along the Adriatic with more than a thousand islands, clear bays, old stone towns and a coast shaped for sailing. From the walls of Dubrovnik to the palace streets of Split, history meets fine food and local wine.</p>
    </div>
    <div class="photo ph-city" style="margin:5px 14px 0;height:72px" role="img" aria-label="Photo of Dubrovnik old town beside a pebble beach"></div>
    <div class="glance">
      <div class="glance-h">Itinerary at a glance</div>
      <table>
        <thead><tr><th>Day</th><th>Date</th><th>Programme</th></tr></thead>
        <tbody>
          <tr><td class="d">D1</td><td class="date">Aug 05, 2023</td><td>Arrival to Dubrovnik, welcome cocktail party on Dubrovnik city walls</td></tr>
          <tr><td class="d">D2</td><td class="date">Aug 06, 2023</td><td>Dubrovnik Highlights city tour – embark, sail to Elafiti</td></tr>
          <tr><td class="d">D3</td><td class="date">Aug 07, 2023</td><td>Sail to Mljet island and day at leisure at sea</td></tr>
          <tr><td class="d">D4</td><td class="date">Aug 08, 2023</td><td>Peljesac Wine Tasting with Live Music – sail to Korcula</td></tr>
          <tr><td class="d">D5</td><td class="date">Aug 09, 2023</td><td>Korcula Highlights Explorer Tour &amp; Local Estate Dinner</td></tr>
          <tr><td class="d">D6</td><td class="date">Aug 10, 2023</td><td>Korcula to Vis Island sail</td></tr>
          <tr><td class="d">D7</td><td class="date">Aug 11, 2023</td><td>Vis Military Tour – sail to Pakleni Islands, Bortelli sunset cocktails</td></tr>
          <tr><td class="d">D8</td><td class="date">Aug 12, 2023</td><td>Hvar island – sail to Split</td></tr>
          <tr><td class="d">D9</td><td class="date">Aug 13, 2023</td><td>Disembark – Split &amp; Trogir ORVALD tours with 6-course wine dinner</td></tr>
          <tr><td class="d">D10</td><td class="date">Aug 14, 2023</td><td>Fly out</td></tr>
        </tbody>
      </table>
      <div class="glance-note">Note: All tours &amp; experiences are optional add ons except the cocktail reception on Dubrovnik city walls.</div>
    </div>
  </section>

  <!-- Itinerary 1-2 -->
  <section class="page" style="left:456px;top:450px">
    <div class="brand">KELVORO</div>
    <div class="head"><div class="kicker">Customised trip</div><div class="title">Itinerary</div><div class="title-rule"></div></div>
    <div class="day"><div><div class="day-top"><span class="num">1</span><span class="day-title">Arrival to Dubrovnik – Welcome cocktail on city walls</span></div><div class="body"><p>August 05, 2023. Private transfer to your hotel, then an exclusive cocktail reception on the city walls with live music and snacks.</p></div></div><div class="photo ph-city" role="img" aria-label="Photo of Dubrovnik rooftops and walls"></div></div>
    <div class="divider"></div>
    <div class="day"><div><div class="day-top"><span class="num">2</span><span class="day-title">Dubrovnik highlights city tour – Embark, sail to Elafiti</span></div><div class="body"><p>August 06, 2023. Morning walk through the old town with a local guide, then board MS Dovetail and sail to the Elafiti islands.</p></div></div><div class="photo ph-sea" role="img" aria-label="Photo of the Elafiti islands coastline"></div></div>
  </section>

  <!-- Itinerary 3-4 -->
  <section class="page" style="left:820px;top:450px">
    <div class="brand">KELVORO</div>
    <div class="head"><div class="kicker">Customised trip</div><div class="title">Itinerary</div><div class="title-rule"></div></div>
    <div class="day"><div><div class="day-top"><span class="num">3</span><span class="day-title">Sail to Mljet island &amp; day at leisure at sea</span></div><div class="body"><p>August 07, 2023. Swim stops in green bays and a slow day on deck near the national park lakes of Mljet.</p></div></div><div class="photo ph-island" role="img" aria-label="Photo of Mljet island lakes and pine forest"></div></div>
    <div class="divider"></div>
    <div class="day"><div><div class="day-top"><span class="num">4</span><span class="day-title">Peljesac wine tasting with live music – Sail to Korcula</span></div><div class="body"><p>August 08, 2023. Taste local reds in a family cellar with live music, then cruise on to Korcula town.</p></div></div><div class="photo ph-green" role="img" aria-label="Photo of Peljesac vineyards"></div></div>
  </section>

  <!-- Itinerary 5-6 -->
  <section class="page" style="left:92px;top:880px">
    <div class="brand">KELVORO</div>
    <div class="head"><div class="kicker">Customised trip</div><div class="title">Itinerary</div><div class="title-rule"></div></div>
    <div class="day"><div><div class="day-top"><span class="num">5</span><span class="day-title">Korcula highlights explorer tour &amp; local estate dinner</span></div><div class="body"><p>August 09, 2023. Discover the walled town of Korcula, then dine at a family estate among olive groves.</p></div></div><div class="photo ph-stone" role="img" aria-label="Photo of Korcula old town"></div></div>
    <div class="divider"></div>
    <div class="day"><div><div class="day-top"><span class="num">6</span><span class="day-title">Korcula to Vis island sail</span></div><div class="body"><p>August 10, 2023. A longer crossing in open water with swim stops and lunch on board before reaching Vis.</p></div></div><div class="photo ph-sea" role="img" aria-label="Photo of a bay on Vis island"></div></div>
  </section>

  <!-- Itinerary 7-8 -->
  <section class="page" style="left:456px;top:880px">
    <div class="brand">KELVORO</div>
    <div class="head"><div class="kicker">Customised trip</div><div class="title">Itinerary</div><div class="title-rule"></div></div>
    <div class="day"><div><div class="day-top"><span class="num">7</span><span class="day-title">Vis military tour – Sail to Pakleni islands, Bortelli sunset cocktails</span></div><div class="body"><p>August 11, 2023. Explore hidden tunnels by jeep, then sail to the Pakleni islands for sunset drinks.</p></div></div><div class="photo ph-island" role="img" aria-label="Photo of the Pakleni islands"></div></div>
    <div class="divider"></div>
    <div class="day"><div><div class="day-top"><span class="num">8</span><span class="day-title">Hvar island – Sail to Split</span></div><div class="body"><p>August 12, 2023. Morning in Hvar town with its fortress and square, then an afternoon cruise to Split.</p></div></div><div class="photo ph-city" role="img" aria-label="Photo of Hvar harbour"></div></div>
  </section>

  <!-- Itinerary 9-10 -->
  <section class="page" style="left:820px;top:880px">
    <div class="brand">KELVORO</div>
    <div class="head"><div class="kicker">Customised trip</div><div class="title">Itinerary</div><div class="title-rule"></div></div>
    <div class="day"><div><div class="day-top"><span class="num">9</span><span class="day-title">Disembark – Split &amp; Trogir ORVALD tours with 6-course wine dinner</span></div><div class="body"><p>August 13, 2023. Walk the palace of Split and the old town of Trogir, then a farewell dinner with local wines.</p></div></div><div class="photo ph-stone" role="img" aria-label="Photo of the old palace in Split"></div></div>
    <div class="divider"></div>
    <div class="day"><div><div class="day-top"><span class="num">10</span><span class="day-title">Transfer to Split airport</span></div><div class="body"><p>August 14, 2023. Private transfer to the airport for your flight home.</p></div></div><div class="photo ph-stone" role="img" aria-label="Photo of Trogir cathedral tower"></div></div>
  </section>

  <!-- Optional post stay -->
  <section class="page" style="left:92px;top:1310px">
    <div class="brand">KELVORO</div>
    <div class="head"><div class="kicker">Customised trip</div><div class="title">Itinerary</div><div class="title-rule"></div></div>
    <div class="day"><div><div class="day-top"><span class="num">+</span><span class="day-title">Optional post stay – 1 night in Velmont 5* hotel</span></div><div class="body"><p>Extend your trip with one night in Split, close to the waterfront and the old town.</p></div></div><div class="photo ph-green" role="img" aria-label="Photo of waterfalls in a national park"></div></div>
    <div class="divider"></div>
    <div class="day"><div><div class="day-top"><span class="num">+</span><span class="day-title">6-course farewell dinner with local wine pairing</span></div><div class="body"><p>A last evening of Dalmatian flavours, each course paired with a wine from the region.</p></div></div><div class="photo ph-dine" role="img" aria-label="Photo of a dinner table set with wine"></div></div>
  </section>

  <!-- Departure -->
  <section class="page" style="left:456px;top:1310px">
    <div class="brand">KELVORO</div>
    <div class="head"><div class="kicker">Customised trip</div><div class="title">Itinerary</div><div class="title-rule"></div></div>
    <div class="day" style="grid-template-columns:1fr"><div><div class="day-top"><span class="num">10</span><span class="day-title">Departure</span></div><div class="body"><p>Transfer to the airport after breakfast. We hope to welcome you on board again soon.</p></div></div></div>
    <div class="grid2">
      <div class="photo ph-dine" style="height:110px" role="img" aria-label="Photo of the yacht dining salon"></div>
      <div class="photo ph-sea" style="height:110px" role="img" aria-label="Photo of the sundeck and sea view"></div>
      <div class="photo ph-stone" style="height:110px;grid-column:span 2" role="img" aria-label="Photo of a stone harbour town at dusk"></div>
    </div>
  </section>

  <!-- Cruise price -->
  <section class="page" style="left:820px;top:1310px">
    <div class="brand">KELVORO</div>
    <div class="head"><div class="kicker">All-inclusive</div><div class="title title-sm">Cruise price</div><div class="title-rule"></div></div>
    <div class="price-box"><span class="yr">2023</span><span class="txt">Aug 05 – Aug 14<br>MS Dovetail</span></div>
    <div class="grid2">
      <div class="photo ph-dine" role="img" aria-label="Photo of a cabin"></div>
      <div class="photo ph-sea" role="img" aria-label="Photo of the deck"></div>
      <div class="photo ph-stone" role="img" aria-label="Photo of the lounge"></div>
      <div class="photo ph-island" role="img" aria-label="Photo of a bay"></div>
    </div>
    <div class="photo ph-ship" style="margin:4px 14px;height:90px" role="img" aria-label="Photo of MS Dovetail under way"></div>
  </section>

  <!-- Price & inclusions -->
  <section class="page" style="left:308px;top:1740px">
    <div class="brand">KELVORO</div>
    <div class="head"><div class="title title-xs">Price &amp; Inclusions</div><div class="title-rule"></div></div>
    <div class="cols">
      <div>
        <div class="list-h">Inclusions</div>
        <ul class="list">
          <li>All transfers per itinerary incl. airport pick up and drop off</li>
          <li>7 nights cruise on MS Dovetail on half board basis</li>
          <li>All meals stated per itinerary</li>
          <li>Captains dinner</li>
          <li>Unlimited water</li>
          <li>Masseuse on board</li>
          <li>Service of 11 crew members</li>
          <li>Cruise director</li>
          <li>Unlimited WiFi</li>
          <li>Daily cleaning</li>
          <li>Arrival refreshments</li>
          <li>Premium docking</li>
          <li>Usage of non motorized water toys</li>
          <li>Exclusive cocktail reception on Dubrovnik city walls with live music and snacks</li>
        </ul>
      </div>
      <div>
        <div class="list-h">Optional tours</div>
        <ul class="list">
          <li>Dubrovnik Highlights Explorer tour</li>
          <li>Peljesac Wine tour with live music</li>
          <li>Korcula explorer tour with local estate dinner</li>
          <li>Vis Military tour</li>
          <li>Bortelli Lounge bar reservation (min spend EUR100 pp)</li>
          <li>Split &amp; Trogir ORVALD Explorer tour</li>
          <li>6-course farewell dinner with local wine pairing</li>
          <li>1 night post stay in Velmont 5* hotel in Split</li>
        </ul>
        <div class="list-h">Extras</div>
        <ul class="list">
          <li>Tips for the crew</li>
          <li>Beverage consumption</li>
          <li>Motorized water toys – EUR150 per hour</li>
          <li>International flights</li>
          <li>Any personal expenses</li>
        </ul>
      </div>
    </div>
    <div style="padding:2px 14px">
      <div class="list-h">Booking conditions</div>
      <div class="body" style="font-size:4.6px">30% non-refundable deposit needed upon confirmation. Balance and any optional tours are due 06 May, 2023.</div>
    </div>
    <div class="photo ph-stone" style="position:absolute;left:0;bottom:0;width:290px;height:70px" role="img" aria-label="Photo of a coastal stone town from above"></div>
  </section>

  <!-- Ship information -->
  <section class="page" style="left:640px;top:1740px">
    <div class="brand">KELVORO</div>
    <div class="head"><div class="title title-xs">Ship Information</div><div class="title-rule"></div></div>
    <div class="body" style="padding:0 14px"><p>MS Dovetail is a modern boutique yacht with elegant cabins, a sundeck, a dining salon and a crew dedicated to a relaxed stay.</p></div>
    <div class="photo ph-dine" style="margin:6px 14px;height:100px" role="img" aria-label="Photo of the yacht salon interior"></div>
    <div style="padding:0 14px" class="list-h">Water sports</div>
    <div class="photo ph-ship" style="margin:4px 14px;height:150px" role="img" aria-label="Photo of the yacht with water toys at the stern"></div>
  </section>

</div>
</body>
</html>
```